TRV business card

Need a business card for a company that provides instructional design and elearning development services. The website is here: http://tarvexa.studio/

I'm attaching a current logo, as well as the old business card design. While I like to keep it clean, the old design is too simplistic for my liking. The only idea I want to reuse from the old design is placing industry jargon on the back of the card, just need a better way to present it. But if you have other ideas for the back--feel free to experiment.

Please use the colors complementary to the color we have on the website. Thank you!

```html
<!DOCTYPE html>
<html lang="en">
<head>
<meta charset="utf-8">
<title>TRV Business Card</title>
<link href="https://fonts.googleapis.com/css2?family=Open+Sans:wght@400;600;700&display=swap" rel="stylesheet">
<style>
  :root {
    --bg: #d9d9d9;
    --teal: #2fb2ab;
    --teal-deep: #17948d;
    --gold: #cbbd86;
    --ink: #3d3d3d;
    --ink-soft: #4a4a4a;
    --paper: #ffffff;
    --paper-shade: #e6e6e6;
  }
  * { margin: 0; padding: 0; box-sizing: border-box; }
  html, body {
    width: 1200px; height: 900px; overflow: hidden;
    background: var(--bg);
    font-family: "Open Sans", Arial, sans-serif;
  }
  .canvas { position: relative; width: 1200px; height: 900px; }
  .card {
    position: absolute; width: 560px; height: 320px;
    overflow: hidden;
    box-shadow: 0 6px 18px rgba(0,0,0,0.25);
  }
  /* Front */
  .card-front {
    left: 80px; top: 90px;
    background: linear-gradient(100deg, var(--paper) 0%, var(--paper) 45%, var(--paper-shade) 100%);
  }
  .brand {
    position: absolute; left: 52px; top: 62px;
    display: flex; align-items: center; gap: 18px;
  }
  .brand-square { width: 58px; height: 58px; background: var(--teal); }
  .brand-name {
    font-weight: 600; font-size: 46px; color: var(--gold);
    letter-spacing: 0.5px; line-height: 1;
  }
  .holder-name {
    position: absolute; left: 0; right: 0; top: 160px;
    text-align: center; padding-left: 150px;
    font-weight: 700; font-size: 23px; color: var(--ink);
  }
  .contact-band {
    position: absolute; left: 0; right: 0; bottom: 0; height: 96px;
    background: linear-gradient(100deg, var(--teal) 0%, var(--teal-deep) 100%);
    color: var(--ink-soft); font-size: 14px;
  }
  .contact-line { position: absolute; white-space: nowrap; }
  .contact-phone { top: 16px; left: 0; right: 0; text-align: center; padding-left: 80px; }
  .contact-web { top: 44px; right: 28px; }
  .contact-mail { top: 70px; left: 26px; }
  .label { color: var(--gold); font-weight: 700; }
  /* Back */
  .card-back {
    left: 560px; top: 480px;
    background: linear-gradient(100deg, var(--teal) 0%, var(--teal-deep) 100%);
  }
  .back-brand {
    position: absolute; left: 0; right: 0; top: 34px;
    display: flex; justify-content: center; align-items: center; gap: 14px;
  }
  .back-brand .brand-square { width: 40px; height: 40px; background: var(--paper); }
  .back-brand .brand-name { font-size: 36px; }
  .help-rule { position: absolute; left: 0; top: 100px; }
  .help-title {
    position: absolute; left: 0; right: 0; top: 118px;
    text-align: center; font-size: 20px; font-weight: 600;
    color: var(--ink); letter-spacing: 0.5px;
  }
  .jargon {
    position: absolute; font-size: 14px; color: var(--ink-soft);
    line-height: 1.55; letter-spacing: 0.8px; text-transform: uppercase;
  }
  .jargon-left { left: 40px; top: 166px; }
  .jargon-right { right: 40px; top: 208px; text-align: right; }
  .jargon span { margin-right: 14px; }
  .jargon-right span { margin-right: 0; margin-left: 14px; }
</style>
</head>
<body>
<div class="canvas">

  <section class="card card-front">
    <div class="brand">
      <div class="brand-square"></div>
      <div class="brand-name">Tarvexa Studio</div>
    </div>
    <div class="holder-name">Daniel Marek</div>
    <div class="contact-band">
      <div class="contact-line contact-phone"><span class="label">T.</span> 646-555-0187</div>
      <div class="contact-line contact-web"><span class="label">W.</span> www.Tarvexa.Studio</div>
      <div class="contact-line contact-mail"><span class="label">E.</span> dmarek@tarvexa.studio</div>
    </div>
  </section>

  <section class="card card-back">
    <div class="back-brand">
      <div class="brand-square"></div>
      <div class="brand-name">Tarvexa Studio</div>
    </div>
    <svg class="help-rule" width="560" height="70" viewBox="0 0 560 70" aria-hidden="true">
      <line x1="40" y1="28" x2="150" y2="28" stroke="#4a4a4a" stroke-width="3"/>
      <line x1="410" y1="50" x2="520" y2="50" stroke="#4a4a4a" stroke-width="3"/>
    </svg>
    <div class="help-title">HOW CAN WE HELP?</div>
    <div class="jargon jargon-left">
      <div><span>Mobile</span><span>Learning</span><span>SCORM</span></div>
      <div><span>Instructional Design</span><span>LMS</span></div>
      <div><span>MOOCs</span><span>eLearning</span><span>HTML5</span></div>
    </div>
    <div class="jargon jargon-right">
      <div><span>Adult</span><span>Learning</span><span>Theory</span></div>
      <div><span>Gamification</span><span>Classroom</span></div>
      <div><span>xAPI</span><span>Blended</span><span>Learning</span></div>
    </div>
  </section>

</div>
</body>
</html>
```